Ridgeway Builders, Inc. Concrete cutting special flyer , 10% off for new customers

Flyer to send to potential customers and business associates and general contractors - specializing in Concrete-Flatwork
Concrete Repair
Concrete Sidewalks
Patios & Driveways
Stoops, Porches And Staircase
Foundation Contractors--Concrete
Facade Restoration
Concrete
Patios
Driveways
Walkways
Commercial Concrete Work
Concrete Restoration
Building Alterations
Foundations - Concrete
Concrete Repairs
rbwxpo.com

Target Market(s)

Homeowners, business owners & general contractors

Industry/Entity Type

Construction

Font styles to use
Serif

Colors
FFC000
F8CF3A
FAE287
FDF2CF
FEFAEE
EB3D1F
EC4F4E
F09395
F8D3D4
FCEDEE

Requirements
Must have
• General Contracting, masonry - Must have Logo Please see list of services Ridgeway Builders NY, Inc., has to offer. Concrete-Flatwork Concrete Repair Concrete Sidewalks Patios & Driveways Stoops, Porches And Staircase Foundation Contractors--Concrete Facade Restoration Concrete Patios Driveways Walkways Commercial Concrete Work Concrete Restoration Building Alterations Foundations - Concrete Concrete Repairs
Nice to have
• List of services - Logo - Black & Gold with a bold color to stand out (preferably reds)

```html
<!DOCTYPE html>
<html lang="en">
<head>
<meta charset="utf-8">
<title>Ridgeway Builders NY, Inc. – Concrete Flatwork Flyer</title>
<link rel="stylesheet" href="https://fonts.googleapis.com/css2?family=Montserrat:wght@400;500;700&display=swap">
<style>
  :root {
    --page-bg: #c8c8c8;
    --paper: #ffffff;
    --red: #df1f46;
    --yellow: #f2bd00;
    --gold-light: #f7cd5a;
    --gold-mid: #e2b04a;
    --gold-dark: #b98a26;
    --tick-bg: #f4b41a;
    --ink: #111111;
    --photo-sky: #c9d3c4;
    --photo-trees: #52613a;
    --photo-soil: #5a4a3a;
  }
  * { margin: 0; padding: 0; box-sizing: border-box; }
  html, body { width: 979px; height: 1200px; overflow: hidden; }
  body { background: var(--page-bg); font-family: "Montserrat", sans-serif; position: relative; }

  .flyer {
    position: absolute; left: 66.5px; top: 0;
    width: 1224px; height: 1736px;
    transform: scale(0.69124); transform-origin: 0 0;
    background: var(--paper); overflow: hidden;
  }
  .flyer__shapes { position: absolute; inset: 0; }

  .brand {
    position: absolute; left: 0; right: 0; top: 60px;
    text-align: center; color: var(--gold-dark);
    font-weight: 700;
  }
  .brand__dot {
    display: block; width: 96px; height: 96px; margin: 0 auto 20px;
    border-radius: 50%; background: var(--gold-dark);
  }
  .brand__name { font-size: 50px; line-height: 1.1; letter-spacing: 1px; }

  .headline {
    position: absolute; left: 66px; top: 883px; width: 1073px; height: 109px;
    border-radius: 55px;
    background: linear-gradient(180deg, var(--gold-light) 0%, var(--gold-mid) 55%, var(--gold-dark) 100%);
    display: flex; align-items: center; justify-content: center;
    font-size: 57px; font-weight: 700; color: var(--ink); letter-spacing: 0.3px;
  }

  .services {
    position: absolute; top: 1040px; list-style: none;
    font-size: 32px; font-weight: 500; color: var(--ink);
  }
  .services--left { left: 53px; }
  .services--right { left: 688px; }
  .services li { display: flex; align-items: center; height: 64px; }
  .tick {
    width: 38px; height: 38px; border-radius: 50%; background: var(--tick-bg);
    margin-right: 14px; flex: none; display: flex; align-items: center; justify-content: center;
  }

  .contact {
    position: absolute; left: 40px; right: 34px; top: 1660px;
    display: flex; justify-content: space-between; align-items: baseline;
    color: #fff; font-size: 38px; font-weight: 400;
  }
  .contact strong { font-weight: 700; }
</style>
</head>
<body>
<div class="flyer">
  <svg class="flyer__shapes" viewBox="0 0 1224 1736" width="1224" height="1736">
    <defs>
      <linearGradient id="site-photo" x1="0" y1="0" x2="0" y2="1">
        <stop offset="0" stop-color="var(--photo-sky)"/>
        <stop offset="0.45" stop-color="var(--photo-trees)"/>
        <stop offset="1" stop-color="var(--photo-soil)"/>
      </linearGradient>
    </defs>
    <rect class="site-photo" role="img" aria-label="Photo of a tracked skid steer loader and an excavator on a cleared dirt job site with trees behind"
          x="0" y="0" width="1224" height="870" fill="url(#site-photo)"/>
    <path d="M0,0 H1224 V15 Q612,565 0,15 Z" fill="var(--paper)"/>
    <path d="M0,15 Q612,565 1224,15 V50 Q612,584 0,50 Z" fill="var(--red)"/>
    <path d="M0,837 Q612,747 1224,837 V867 Q612,777 0,867 Z" fill="var(--red)"/>
    <path d="M0,867 Q612,777 1224,867 V1736 H0 Z" fill="var(--paper)"/>
    <path d="M0,1482 Q612,1682 1224,1482 V1736 H0 Z" fill="var(--yellow)"/>
    <path d="M0,1522 Q612,1718 1224,1522 V1736 H0 Z" fill="var(--red)"/>
  </svg>

  <div class="brand">
    <span class="brand__dot"></span>
    <div class="brand__name">Ridgeway Builders<br>NY, Inc.</div>
  </div>

  <div class="headline">Specializing in Concrete Flatwork</div>

  <ul class="services services--left">
    <li><span class="tick"><svg width="20" height="16" viewBox="0 0 20 16"><path d="M3,8 L8,13 L17,3" fill="none" stroke="var(--red)" stroke-width="3"/></svg></span>Concrete Repair</li>
    <li><span class="tick"><svg width="20" height="16" viewBox="0 0 20 16"><path d="M3,8 L8,13 L17,3" fill="none" stroke="var(--red)" stroke-width="3"/></svg></span>Concrete Sidewalks</li>
    <li><span class="tick"><svg width="20" height="16" viewBox="0 0 20 16"><path d="M3,8 L8,13 L17,3" fill="none" stroke="var(--red)" stroke-width="3"/></svg></span>Patios &amp; Driveways</li>
    <li><span class="tick"><svg width="20" height="16" viewBox="0 0 20 16"><path d="M3,8 L8,13 L17,3" fill="none" stroke="var(--red)" stroke-width="3"/></svg></span>Stoops, Porches and Staircase</li>
    <li><span class="tick"><svg width="20" height="16" viewBox="0 0 20 16"><path d="M3,8 L8,13 L17,3" fill="none" stroke="var(--red)" stroke-width="3"/></svg></span>Foundation Contractors - Concrete</li>
    <li><span class="tick"><svg width="20" height="16" viewBox="0 0 20 16"><path d="M3,8 L8,13 L17,3" fill="none" stroke="var(--red)" stroke-width="3"/></svg></span>Facade Restoration</li>
    <li><span class="tick"><svg width="20" height="16" viewBox="0 0 20 16"><path d="M3,8 L8,13 L17,3" fill="none" stroke="var(--red)" stroke-width="3"/></svg></span>Concrete</li>
  </ul>

  <ul class="services services--right">
    <li><span class="tick"><svg width="20" height="16" viewBox="0 0 20 16"><path d="M3,8 L8,13 L17,3" fill="none" stroke="var(--red)" stroke-width="3"/></svg></span>Driveways</li>
    <li><span class="tick"><svg width="20" height="16" viewBox="0 0 20 16"><path d="M3,8 L8,13 L17,3" fill="none" stroke="var(--red)" stroke-width="3"/></svg></span>Walkways</li>
    <li><span class="tick"><svg width="20" height="16" viewBox="0 0 20 16"><path d="M3,8 L8,13 L17,3" fill="none" stroke="var(--red)" stroke-width="3"/></svg></span>Commercial Concrete Work</li>
    <li><span class="tick"><svg width="20" height="16" viewBox="0 0 20 16"><path d="M3,8 L8,13 L17,3" fill="none" stroke="var(--red)" stroke-width="3"/></svg></span>Concrete Restoration</li>
    <li><span class="tick"><svg width="20" height="16" viewBox="0 0 20 16"><path d="M3,8 L8,13 L17,3" fill="none" stroke="var(--red)" stroke-width="3"/></svg></span>Building Alterations</li>
    <li><span class="tick"><svg width="20" height="16" viewBox="0 0 20 16"><path d="M3,8 L8,13 L17,3" fill="none" stroke="var(--red)" stroke-width="3"/></svg></span>Foundation Concrete</li>
    <li><span class="tick"><svg width="20" height="16" viewBox="0 0 20 16"><path d="M3,8 L8,13 L17,3" fill="none" stroke="var(--red)" stroke-width="3"/></svg></span>Concrete Repairs</li>
  </ul>

  <div class="contact">
    <span class="contact__phone">Call or Text <strong>516-555-0142 or 516-555-0187</strong></span>
    <span class="contact__web">www.rbwxpo.com</span>
  </div>
</div>
</body>
</html>
```